Newsletter for a recent surgical mission conducted by Bright Shores Relief

We need a one page, two sided newsletter reporting the events of our recent mission trip. The first page should have the title Bright Shores Relief along with the mission date of November 2019 and Cayo, Belize as the location. We want to highlight the pictures of the children especially the before and after pictures. Pictures of the hospital and ward should give the viewer the feel that they visited the hospital with us and to show how basic and rustic it is. Maybe stock photos of mountainous green landscape would help.

Target Market(s)

Our donors receive this and we want to highlight what we did and how their contributions enabled us to do it.

Industry/Entity Type

Non Profit

Font styles to use
Sans Serif

Colors

Designer to choose colors to be used in the design.

Requirements
Must have
• 1. The organization logo
• 2. Please match the text describing each patient to the corresponding pictures of the patients.
• 3. Highlighted text thanking our donors for donating.
• 4. www.brightshoresrelief should be included which is our website.
• 5. Text asking anyone who wants to contribute to our next mission to visit the Donate link on our website.
Nice to have
• 1. Stock images of the Belizean landscape can be used along with the picture of the hospital.
• 2. I am not sure what 'GREYSCALE" is but it might be interesting to see what a version of the newsletter looks like in that color. We have always matched the colors in the logo. If not, then just match the colors in the logo but let the designer choose.
Should not have
• When including the picture of us the surgeons, keep it small. We want to highlight the patients NOT the staff.

```html
<!DOCTYPE html>
<html lang="en">
<head>
<meta charset="utf-8">
<title>Bright Shores Relief – November 2019 Newsletter</title>
<link href="https://fonts.googleapis.com/css2?family=Arimo:wght@400;700&display=swap" rel="stylesheet">
<style>
:root{
  --blue:#1762ad;
  --blue-deep:#0f57a0;
  --green:#4f8a3e;
  --white:#ffffff;
  --paper:#ffffff;
}
*{margin:0;padding:0;box-sizing:border-box}
html,body{width:1200px;height:800px;overflow:hidden;background:var(--paper)}
body{position:relative;font-family:"Arimo",Arial,sans-serif;color:var(--white)}
.abs{position:absolute}
.page{position:absolute;background:var(--blue)}
.panel-green{position:absolute;background:var(--green)}
.panel-blue{position:absolute;background:var(--blue)}
.photo{position:absolute}
.body-text{position:absolute;font-size:9px;line-height:1.3;color:var(--white)}
.body-text.lg{font-size:11px;line-height:1.25}
.tag{position:absolute;background:var(--blue);color:var(--white);font-size:7.5px;padding:2px 5px;letter-spacing:.2px}
.tag.plain{background:transparent;color:#c7a84a}
.masthead-rule{position:absolute;left:93px;top:78px;width:2px;height:135px;background:var(--white)}
.masthead-title{position:absolute;left:107px;top:84px;font-size:28.5px;font-weight:400;letter-spacing:.3px;white-space:nowrap}
.masthead-sub{position:absolute;left:108px;font-size:18px}
.web{position:absolute;font-size:12px;color:var(--white)}
.logo-box{position:absolute;left:462px;top:64px;width:114px;height:84px;background:var(--white);display:flex;flex-direction:column;align-items:center;justify-content:center;gap:6px}
.logo-dot{width:18px;height:18px;border-radius:50%;background:var(--green)}
.logo-name{font-size:10.5px;font-weight:700;color:var(--green);text-align:center;line-height:1.2}
.cloud{position:absolute}
.cloud-text{position:absolute;font-size:11px;line-height:1.3;color:var(--white)}
.donate-note{position:absolute;font-size:6.5px;line-height:1.3;color:var(--white);border-left:1.5px solid var(--white);padding-left:4px}
</style>
</head>
<body>

<!-- Front page -->
<section class="page" style="left:22px;top:50px;width:567px;height:708px"></section>

<div class="photo" role="img" aria-label="Tropical beach with palm trees and a white seaside house under a blue sky"
     style="left:36px;top:64px;width:540px;height:148px;background:linear-gradient(180deg,#3d72c4 0%,#8fb4e4 45%,#c9dcef 62%,#4f7a3a 78%,#2f5a2a 100%)"></div>
<div class="masthead-rule"></div>
<h1 class="masthead-title">BRIGHT SHORES RELIEF</h1>
<p class="masthead-sub" style="top:118px">November 2019</p>
<p class="masthead-sub" style="top:138px">Cayo, Belize</p>
<p class="web" style="left:408px;top:190px">www.brightshoresrelief.com</p>
<div class="logo-box"><span class="logo-dot"></span><span class="logo-name">Bright Shores<br>Relief</span></div>

<div class="panel-green" style="left:36px;top:212px;width:540px;height:68px"></div>
<p class="body-text" style="left:108px;top:222px;width:420px">The Bright Shores Relief Team returned to the Cayo District of Belize for a weeklong mission working with the staffs of the Riverside Community Hospital and the Central Valley Medical Center in Belmopan. The Team performed primarily cleft lip and palate surgery which is not readily available to children in need throughout the country.</p>

<div class="panel-blue" style="left:36px;top:280px;width:540px;height:228px"></div>
<p class="body-text" style="left:51px;top:291px;width:365px">This is Lena Morales from the small town of Spanish Lookout in Cayo, Belize. Lena is 5 months old and was born with a cleft lip and palate. The Team was able to help her by performing the 1st of 4 surgeries she will need to reconstruct her lip, palate and nose.</p>
<div class="photo" role="img" aria-label="Before photo: infant with cleft lip wrapped in a towel" style="left:51px;top:346px;width:115px;height:141px;background:linear-gradient(160deg,#c9c2b8,#e8e4de 60%,#b6b4c0)"></div>
<span class="tag" style="left:51px;top:334px">BEFORE</span>
<div class="photo" role="img" aria-label="After photo: infant after cleft lip repair" style="left:172px;top:346px;width:115px;height:141px;background:linear-gradient(160deg,#9a6a5c,#d9c8bc 55%,#cfd3d8)"></div>
<span class="tag" style="left:172px;top:333px">AFTER</span>
<div class="photo" role="img" aria-label="Father holding his baby daughter in the hospital ward" style="left:292px;top:335px;width:114px;height:152px;background:linear-gradient(170deg,#5a8f4a,#8e3a3a 55%,#3e5b72)"></div>
<div class="photo" role="img" aria-label="Surgical team members in scrubs standing together" style="left:422px;top:280px;width:154px;height:216px;background:linear-gradient(180deg,#d8d0c4,#3f5f9e 55%,#2e4f8c)"></div>
<span class="tag plain" style="left:534px;top:281px">BSR TEAM</span>

<div class="panel-green" style="left:36px;top:509px;width:540px;height:237px"></div>
<p class="body-text" style="left:50px;top:520px;width:246px">This is Ramon Castillo, a 23 year old man from the town of Santa Elena in Cayo. He sustained a left upper arm injury from a rotating saw four years ago that lacerated his radial nerve. It was never repaired and now he cannot extend his wrist, thumb and fingers. The Team performed forearm muscle and tendon transfers which after a 6-week recovery will allow him to get back to work doing construction.</p>
<div class="photo" role="img" aria-label="Patient's bandaged forearm resting on hospital linen" style="left:302px;top:517px;width:128px;height:171px;background:linear-gradient(160deg,#b9b7b2,#ecebe7 55%,#d6d4cf)"></div>
<div class="photo" role="img" aria-label="Surgeon sitting beside the patient in a hospital bed" style="left:439px;top:517px;width:128px;height:171px;background:linear-gradient(170deg,#c8c6c0,#2d56a0 55%,#d7d7d2)"></div>

<svg class="cloud" style="left:26px;top:632px" width="282" height="78" viewBox="0 0 282 78" aria-hidden="true">
  <g fill="var(--blue)">
    <ellipse cx="141" cy="42" rx="136" ry="28"/>
    <ellipse cx="60" cy="38" rx="52" ry="30"/>
    <ellipse cx="150" cy="30" rx="70" ry="28"/>
    <ellipse cx="235" cy="36" rx="44" ry="30"/>
  </g>
</svg>
<p class="cloud-text" style="left:50px;top:652px;width:250px">Many thanks to ALL those who donated in support of our mission, enabling us to provide life changing surgery and positively impact so many lives.</p>
<div class="photo" role="img" aria-label="Aerial view of lush green Belizean forest" style="left:300px;top:697px;width:276px;height:49px;background:linear-gradient(90deg,#2f6a2a,#4f8f3a 50%,#2c5f27)"></div>

<!-- Back page -->
<section class="page" style="left:615px;top:50px;width:567px;height:708px"></section>
<div class="panel-green" style="left:630px;top:63px;width:532px;height:681px"></div>

<div class="photo" role="img" aria-label="Before photo: crying infant with severe cleft lip" style="left:645px;top:70px;width:149px;height:188px;background:linear-gradient(170deg,#d24a7a,#e4c2ac 50%,#c9ccd6)"></div>
<span class="tag" style="left:645px;top:70px;background:var(--green)">BEFORE</span>
<div class="photo" role="img" aria-label="After photo: infant following cleft lip repair" style="left:645px;top:280px;width:149px;height:186px;background:linear-gradient(170deg,#e8e6e2,#c59a80 50%,#3a3a3a)"></div>
<span class="tag" style="left:645px;top:267px;background:var(--green)">AFTER</span>
<div class="photo" role="img" aria-label="Mother holding her infant son on her lap" style="left:643px;top:476px;width:151px;height:200px;background:linear-gradient(170deg,#dcd7cf,#8a6a55 45%,#2b2b30)"></div>

<div class="photo" role="img" aria-label="Colourful welcome sign above the pediatric ward entrance" style="left:809px;top:63px;width:353px;height:75px;background:linear-gradient(180deg,#d9e2dc,#c3d6c6)"></div>
<p class="body-text lg" style="left:813px;top:143px;width:330px">This is Tavi Chel and his mother, Marisol. Tavi is 7 months old and was born with a severe cleft lip. His mom brought him to see us and the Team was able to repair his cleft lip this week before they head back to their home in Stann Creek, Cayo</p>

<div class="panel-blue" style="left:809px;top:205px;width:353px;height:239px"></div>
<p class="body-text lg" style="left:812px;top:209px;width:348px">The Central Valley Medical Center in Belmopan is the secondary receiving center for all of the smaller community hospitals and clinics throughout all of the Cayo District. It maintains a large clinic system, Emergency Room, two operating rooms, and an adult, maternity, and pediatric ward totaling 40 beds. The BSR Team was fortunate to partner with the doctors and staff there doing our work.</p>
<div class="photo" role="img" aria-label="Surgeons operating under theatre lights" style="left:822px;top:298px;width:106px;height:142px;background:linear-gradient(170deg,#d8dad4,#3f8a6a 50%,#2f6a5a)"></div>
<div class="photo" role="img" aria-label="Simple pediatric ward with beds and green walls" style="left:933px;top:298px;width:107px;height:142px;background:linear-gradient(170deg,#9ccf6a,#c9cfd2 55%,#9a8a7a)"></div>
<div class="photo" role="img" aria-label="Exterior of the medical center under a cloudy sky" style="left:1046px;top:298px;width:116px;height:88px;background:linear-gradient(180deg,#2f6fc4,#bcd3ee 55%,#6c8a4c)"></div>
<p class="donate-note" style="left:1046px;top:396px;width:116px">Anyone who wants to contribute to our next mission visit the Donate link on our website:<br><span style="font-size:5px">www.brightshoresrelief.com/donate/</span></p>

<p class="body-text lg" style="left:827px;top:455px;width:325px">This is 5 year old Elvin Reyes with his Mom and Dad. They are from the Frank's Eddy Village in Belize. Elvin had his cleft lip and palate repaired when he was younger. Unfortunately, he developed an opening in the roof of his mouth afterwards (palatal fistula) that results in liquid and food in his mouth coming out his nose when he ate. The Team was able to repair his palate this week and in a short time get back to eating normally.</p>
<div class="photo" role="img" aria-label="Young boy in a blue surgical cap before his operation" style="left:846px;top:555px;width:136px;height:183px;background:linear-gradient(170deg,#7fb7e4,#c99a7e 45%,#e6e6e6)"></div>
<div class="photo" role="img" aria-label="Boy standing with his mother and father in the ward" style="left:998px;top:558px;width:138px;height:180px;background:linear-gradient(170deg,#e6e4e0,#c94a5a 45%,#3a4a6a)"></div>

<svg class="cloud" style="left:622px;top:676px" width="216" height="82" viewBox="0 0 216 82" aria-hidden="true">
  <g fill="var(--blue)">
    <ellipse cx="108" cy="50" rx="104" ry="30"/>
    <ellipse cx="48" cy="42" rx="42" ry="32"/>
    <ellipse cx="120" cy="34" rx="58" ry="30"/>
    <ellipse cx="180" cy="44" rx="34" ry="30"/>
    <rect x="4" y="50" width="208" height="32"/>
  </g>
</svg>
<p class="web" style="left:653px;top:722px;font-size:12px">www.brightshoresrelief.com</p>

</body>
</html>
```